New A4 Flyer for Occupational Health Clinic offering Regional (Country/Rural) Telehealth service

We are an occupational health clinic, launching a regional telehealth occupational health service aimed at regional (country/rural) areas in South Australia, where employers and workers can get access to telehealth appointments with our doctors within 24 hours of request.

The name of the service is called Regional Telehealth. We need this brochure by noon Wednesday 26th April (Adelaide time, Australia). Please advise us ASAP it this is not achievable.

I have explained the model below and attached a flowchart which would be good to be included in the 2nd page and made to look 'designer material'

1) Remote worker books telehealth with doctor
2) Worker is booked in to local physios in the area. 3-way consult (worker and physio on one end, doctor on the other) happens.
3) Doctor travels down to regional area once a month for face to face review and to look at workplace (worksite visit) if needed.
4) We also offer Second Opinion Medicine and Independent Medical exam face to face if requested.

Please see attached previous flyers - we would like to see designs that show 'non-medical' ie non threatening, no white coats, no people in pain or injury. We want to portray a positive vibe, smiles, healing and wellness.

The main message is HOPE to our customers.

Please see out website and pics to understand our messaging

www.kelvaro.com.au.

We have a specific page for telehealth:

https://kelvaro.com.au/what-we-do/telehealth

Our colour is green.

The target industries in the area in order of size are :
1) Timber industries
2) Food processing (meat > dairy)
3) Farming
3) Aged care and retail (supermarkets etc)

We would like the front page to show a regional worker (this is important), at home or at work, with or without a device, sending a message of hope.

We like the photos below, but happy for you to suggest as well :

https://www.pictavault.com/photos/free-man-with-open-arms-in-wheat-field-at-sunset

https://www.pictavault.com/photo/father-sitting-next-to-laptop-and-holding-son-on-his-lap-gm5839104726-914027385

A good example of teleheath website is here :

https://www.curalinkhub.com.au/online-doctors/

Please scroll down to see "how it works". We like the 4 step "flow chart. which we would like our flowchart attached to look like. (Their photos are also good examples.)

We also need to add the following texts from our older brochures although there has been some changes . Same font and spacing would be nice for 1)

1)
DEDICATED TO YOUR FUTURE
Specialists in Occupational
Healthcare and Return to Work
BRENWICK
ELM VALE
TELEHEALTH

2) BENEFITS OF USING US:
- We provide new injury appointments within 24 hours. (this is new)
- We communicate and dedicate time to fulfil your needs.
- We provide tailored and personalised care.
- We are South Australian.
- We are dedicated to your future.

3) WE ACHIEVE RESULTS:
- 60% of injured workers recover & return to normal duties after 1 week.
- 75% of injured workers recover & return to normal duties after 2 weeks.
- Up to 50% faster recovery & return to normal duties.
- Up to 40% reduction in claims costs in the first year.
- 0% reduction in total average days off work.

4) Other services we provide :

a) Second Opinion Medicine
- Helping provide GPs and injured workers fast and easy access to South Australia's top medical specialists.

b) Fitness for Duty Assessments
- Ensuring workers are able to work safely after illness or injury.

c) Independent Medical Examination
- Providing clarity and direction for claims management through independent expert opinion on causation, capacity for work and treatment

d) Pre-employment and periodic medical examination
- Helping employers recruit the best fit for their organisation

e) Permanent Impairment Assessment
- Providing worker's, insurers and employers with expert opinion to help understand and quantify loss of function due to injury.

Please add "Please contact our office for further information about the above services."

Contact Us
admin@kelvaro.com.au (08) 7459 2637 www.kelvaro.com.au

(no address needed)

Target Market(s)

Employers, Insurers and Workers (Patients)

Industry/Entity Type

Medical

Font styles to use
Sans Serif
Other font styles liked:
• Please see attached old flyers

Colors
00AB8E
00BBA5
67D7C9
C6EFE9
E9F9F6

Requirements
Must have
• Green (as per logo) and Rural workers. Deviced - laptop, ipad or phone
Nice to have
• Smiles, positive energy, healing, recovery and wellness. Please see link to website and photos
Should not have
• White coats, people in pain, negative messaging. The meesage should be "non-medical"

```html
<!DOCTYPE html>
<html lang="en">
<head>
<meta charset="utf-8">
<title>Kelvaro Occupational Medicine – Regional Telehealth Flyer</title>
<link href="https://fonts.googleapis.com/css2?family=Montserrat:wght@400;500;600;700&display=swap" rel="stylesheet">
<style>
:root{
  --teal:#3daf98;
  --teal-dark:#2f9a84;
  --mint:#bde3dd;
  --mint-soft:#c9ebe5;
  --ink:#1f2523;
  --grey:#555c5a;
  --arrow:#4a4f4e;
  --backdrop:#c8c8c8;
  --white:#ffffff;
}
*{box-sizing:border-box;margin:0;padding:0}
html,body{width:1200px;height:694px;overflow:hidden;background:var(--backdrop);font-family:'Montserrat',sans-serif;color:var(--ink)}
.canvas{position:relative;width:1200px;height:694px}
.sheet{position:absolute;background:var(--white);overflow:hidden;box-shadow:-6px 6px 10px rgba(0,0,0,.35)}
.abs{position:absolute}

/* brand */
.brand{position:absolute;display:flex;align-items:center;gap:6px}
.brand-dot{width:45px;height:45px;border-radius:50%;background:var(--teal);opacity:.75;flex:none}
.brand-name{color:#4d5352;font-weight:500;line-height:1.05}
.brand-name .big{display:block;font-size:22px;letter-spacing:.5px}
.brand-name .small{display:block;font-size:8.4px;letter-spacing:.3px}

/* front page */
.front{left:49px;top:37px;width:438px;height:619px}
.front .hero-band{left:0;top:79px;width:438px;height:172px;background:var(--teal)}
.front .photo-ring{left:178px;top:-112px;width:282px;height:282px;border-radius:50%;background:var(--mint)}
.front .photo{left:188px;top:-102px;width:262px;height:262px;border-radius:50%;
  background:radial-gradient(circle at 60% 45%,#6d8fb8 0%,#8a7760 45%,#4d4438 100%)}
.front .photo-fill{left:320px;top:0;width:118px;height:60px;background:linear-gradient(#7a6a58,#6d8fb8)}
.pill{left:13px;top:100px;height:17px;padding:0 9px;background:var(--white);border-radius:9px;color:var(--teal);font-size:9px;font-weight:600;line-height:17px;letter-spacing:.3px}
.headline{left:15px;top:123px;color:var(--white);font-weight:700;font-size:20.5px;line-height:23.7px;letter-spacing:.2px}
.locations{left:14px;top:229px;color:var(--white);font-size:8.3px;font-weight:600;letter-spacing:.2px;display:flex;gap:6px}
.results-tab{left:0;top:254px;width:190px;height:21px}
.results-title{left:19px;top:256px;font-size:11px;font-weight:700;letter-spacing:.2px}
.ticks{list-style:none;left:17px;top:284px;font-size:8.7px;line-height:14.8px;color:#2c3230}
.ticks li{display:flex;align-items:center;gap:5px}
.tick{width:7px;height:7px;flex:none}
.services{left:0;top:365px;width:438px;height:210px;background:var(--mint);border-top:2px solid var(--teal)}
.services-tab{left:0;top:365px;width:202px;height:23px}
.services-title{left:22px;top:369px;color:var(--white);font-size:11.2px;font-weight:600}
.svc{position:absolute;width:190px}
.svc h3{font-size:10.4px;font-weight:700;color:#262b2a;line-height:14px;display:flex;gap:6px}
.svc h3::before{content:"";width:4px;height:4px;border-radius:50%;background:var(--teal);margin-top:5px;flex:none}
.svc p{font-size:8.2px;line-height:11.8px;color:#3a403e;margin-top:3px}
.col-rule{left:219px;top:394px;width:1px;height:121px;background:#555}
.footer{background:var(--teal);color:var(--white);display:flex;align-items:center}
.front .footer{left:0;top:575px;width:438px;height:44px}
.contact{position:absolute;display:flex;align-items:center;gap:4px;font-size:8.3px;font-weight:500}
.contact.phone{font-size:11.5px;font-weight:700}
.contact svg{width:9px;height:9px;fill:var(--white)}

/* back page */
.back{left:529px;top:147px;width:610px;height:431px}
.benefits-title{left:232px;top:16px;font-size:9.6px;font-weight:700;letter-spacing:.2px}
.benefits{list-style:none;position:absolute;top:34px;left:0;font-size:8.6px;line-height:14.4px;color:#2c3230}
.benefits li{display:flex;align-items:center;gap:4px;position:relative}
.step{position:absolute;width:67px;display:flex;align-items:center;justify-content:center;text-align:center}
.step.top{top:123px;height:72px;background:var(--mint);font-size:6.3px;font-weight:700;line-height:7.9px;color:#2c3230;align-items:flex-start;padding:8px 3px 0}
.step.end{font-size:10px;line-height:12px;align-items:center;padding:0}
.step.detail{top:200px;height:179px;background:var(--teal);color:var(--white);font-size:6.1px;font-weight:700;line-height:7.8px;align-items:flex-start;padding:13px 4px 0}
.step.detail p+p{margin-top:7.8px}
.arrow{position:absolute;width:13px;height:13px}
.stetho{left:15px;top:295px;width:72px;height:82px;background:linear-gradient(135deg,#f0f0f0,#dcdcdc);border-radius:40px 10px 40px 40px}
.back .footer{left:0;top:388px;width:610px;height:43px}
</style>
</head>
<body>
<div class="canvas">

  <!-- FRONT PAGE -->
  <section class="sheet front" aria-label="Front page">
    <div class="abs hero-band"></div>
    <div class="abs photo-ring"></div>
    <div class="abs photo-fill" role="img" aria-label="Photo of a father in a hard hat with his son by a laptop"></div>
    <div class="abs photo" role="img" aria-label="Photo of a father in a hard hat with his son by a laptop"></div>

    <div class="brand" style="left:14px;top:18px">
      <div class="brand-dot"></div>
      <div class="brand-name"><span class="big">KELVARO</span><span class="small">OCCUPATIONAL MEDICINE</span></div>
    </div>

    <div class="abs pill">DEDICATED TO YOUR FUTURE</div>
    <h1 class="abs headline">Specialists in<br>Occupational<br>Healthcare and<br>Return to Work</h1>
    <div class="abs locations"><span>• BRENWICK</span><span>• ELM VALE</span><span>• TELEHEALTH</span></div>

    <svg class="abs results-tab" viewBox="0 0 190 21" preserveAspectRatio="none"><polygon points="0,0 190,0 182,21 0,21" fill="var(--mint)"/></svg>
    <h2 class="abs results-title">WE ACHIEVE RESULTS:</h2>
    <ul class="abs ticks">
      <li><svg class="tick" viewBox="0 0 10 10"><path d="M1 5.5 4 8.5 9 1.5" stroke="var(--teal)" stroke-width="2" fill="none"/></svg>60% of injured workers recover &amp; return to normal duties after 1 week.</li>
      <li><svg class="tick" viewBox="0 0 10 10"><path d="M1 5.5 4 8.5 9 1.5" stroke="var(--teal)" stroke-width="2" fill="none"/></svg>75% of injured workers recover &amp; return to normal duties after 2 weeks.</li>
      <li><svg class="tick" viewBox="0 0 10 10"><path d="M1 5.5 4 8.5 9 1.5" stroke="var(--teal)" stroke-width="2" fill="none"/></svg>Up to 50% faster recovery &amp; return to normal duties.</li>
      <li><svg class="tick" viewBox="0 0 10 10"><path d="M1 5.5 4 8.5 9 1.5" stroke="var(--teal)" stroke-width="2" fill="none"/></svg>Up to 40% reduction in claims costs in the first year.</li>
      <li><svg class="tick" viewBox="0 0 10 10"><path d="M1 5.5 4 8.5 9 1.5" stroke="var(--teal)" stroke-width="2" fill="none"/></svg>0% reduction in total average days off work.</li>
    </ul>

    <div class="abs services"></div>
    <svg class="abs services-tab" viewBox="0 0 202 23" preserveAspectRatio="none"><polygon points="0,0 202,0 195,23 0,23" fill="var(--teal)"/></svg>
    <h2 class="abs services-title">Other services we provide :</h2>
    <div class="abs col-rule"></div>

    <div class="svc" style="left:17px;top:395px"><h3>Second Opinion Medicine</h3><p>Helping provide GPs and injured workers fast and easy access to South Australia's top medical specialists.</p></div>
    <div class="svc" style="left:17px;top:454px;width:200px"><h3>Independent Medical Examination</h3><p>Providing clarity and direction for claims management through independent expert opinion on causation, capacity for work and treatment</p></div>
    <div class="svc" style="left:228px;top:395px"><h3>Fitness for Duty Assessments</h3><p>Ensuring workers are able to work safely after illness or injury.</p></div>
    <div class="svc" style="left:228px;top:454px;width:180px"><h3>Pre-employment and periodic medical examination</h3><p>Helping employers recruit the best fit for their organisation</p></div>
    <div class="svc" style="left:17px;top:526px;width:410px"><h3>Permanent Impairment Assessment</h3><p>Providing worker's, insurers and employers with expert opinion to help understand and quantify loss of function due to injury.</p></div>

    <footer class="abs footer">
      <span class="contact phone" style="left:22px"><svg viewBox="0 0 10 10"><path d="M2 0.5 3.8 2.6 3 4a6 6 0 0 0 3 3l1.4-.8L9.5 8 8.3 9.5C4 9 1 6 .5 1.7z"/></svg>(08) 7459 2637</span>
      <span class="contact" style="left:173px"><svg viewBox="0 0 10 10"><circle cx="5" cy="5" r="4.2" fill="none" stroke="#fff" stroke-width="1"/><path d="M.8 5h8.4M5 .8c-2.4 2.5-2.4 5.9 0 8.4M5 .8c2.4 2.5 2.4 5.9 0 8.4" fill="none" stroke="#fff" stroke-width=".8"/></svg>www.kelvaro.com.au</span>
      <span class="contact" style="left:310px"><svg viewBox="0 0 10 8"><rect x=".5" y=".5" width="9" height="7" fill="#fff"/><path d="M.5 .8 5 4.5 9.5 .8" fill="none" stroke="var(--teal)" stroke-width=".9"/></svg>admin@kelvaro.com.au</span>
    </footer>
  </section>

  <!-- BACK PAGE -->
  <section class="sheet back" aria-label="Back page">
    <svg class="abs" style="left:0;top:0" width="610" height="114" viewBox="0 0 610 114"><polygon points="199,0 610,0 610,114 233,114" fill="var(--mint)"/></svg>

    <div class="brand" style="left:16px;top:35px">
      <div class="brand-dot"></div>
      <div class="brand-name"><span class="big">KELVARO</span><span class="small">OCCUPATIONAL MEDICINE</span></div>
    </div>

    <h2 class="abs benefits-title">BENEFITS OF USING US:</h2>
    <ul class="benefits">
      <li style="left:234px"><svg class="tick" viewBox="0 0 10 10"><path d="M1 5.5 4 8.5 9 1.5" stroke="var(--teal)" stroke-width="2" fill="none"/></svg>We provide new injury appointments within 24 hours. (this is new)</li>
      <li style="left:238px"><svg class="tick" viewBox="0 0 10 10"><path d="M1 5.5 4 8.5 9 1.5" stroke="var(--teal)" stroke-width="2" fill="none"/></svg>We communicate and dedicate time to fulfil your needs.</li>
      <li style="left:243px"><svg class="tick" viewBox="0 0 10 10"><path d="M1 5.5 4 8.5 9 1.5" stroke="var(--teal)" stroke-width="2" fill="none"/></svg>We provide tailored and personalised care.</li>
      <li style="left:247px"><svg class="tick" viewBox="0 0 10 10"><path d="M1 5.5 4 8.5 9 1.5" stroke="var(--teal)" stroke-width="2" fill="none"/></svg>We are South Australian.</li>
      <li style="left:252px"><svg class="tick" viewBox="0 0 10 10"><path d="M1 5.5 4 8.5 9 1.5" stroke="var(--teal)" stroke-width="2" fill="none"/></svg>We are dedicated to your future.</li>
    </ul>

    <!-- flow: top row -->
    <div class="step top end" style="left:17px">New<br>injury<br>or<br>claim</div>
    <div class="step top" style="left:89px">Book your Appointment</div>
    <div class="step top" style="left:162px">Online appointment with Kelvaro expert medical specialist</div>
    <div class="step top" style="left:235px">Online Kelvaro physiotherapy appointment if needed</div>
    <div class="step top" style="left:307px">In person appointment with top local physiotherapist</div>
    <div class="step top" style="left:380px">Online review appointments with doctor and in person treatment with local physiotherapist</div>
    <div class="step top" style="left:452px">Monthly in person appointment with doctor in local region</div>
    <div class="step top end" style="left:525px">Recovery<br>and<br>Return<br>to Work</div>

    <!-- flow: details -->
    <div class="step detail" style="left:89px"><div><p>Call 08 7459 2637 or email admin@ kelvaro.com.au.</p><p>Video consults are preferred to phone consults.</p></div></div>
    <div class="step detail" style="left:162px"><div><p>Prescriptions are delivered to worker's phone or local pharmacy.</p><p>Employer and/or insurer are contacted to discuss diagnosis and plan.</p><p>Work Capacity certificates are issued to worker, employer and insurer.</p></div></div>
    <div class="step detail" style="left:235px"><div><p>This is offered if a local physiotherapy appointment cannot be accommodated within 7 days.</p></div></div>
    <div class="step detail" style="left:307px"><div><p>A 3-way consult between worker, doctor and physiotherapist is conducted to confirm diagnosis and implement treatment program</p><p>Employer and/or insurer are updated on worker's progress.</p></div></div>
    <div class="step detail" style="left:380px"><div><p>Any workers requiring more specialised medical services will travel to Adelaide for treatment</p><p>Second Opinion Medicine and Independent Medical Examination can be provided at local regional areas on request.</p></div></div>
    <div class="step detail" style="left:452px"><div><p>Our team of doctors will travel to local regional areas monthly to review workers in person</p><p>Our doctors can also conduct worksite visits to familiarise ourselves with worker's duties and the employer's business.</p></div></div>

    <div class="abs stetho" role="img" aria-label="Stethoscope illustration"></div>

    <!-- arrows -->
    <svg width="0" height="0" style="position:absolute"><defs>
      <symbol id="arrow-right" viewBox="0 0 14 14"><circle cx="7" cy="7" r="7" fill="var(--arrow)"/><path d="M3.5 7h7M7.5 4 10.5 7 7.5 10" stroke="#fff" stroke-width="1.3" fill="none"/></symbol>
      <symbol id="arrow-down" viewBox="0 0 14 14"><circle cx="7" cy="7" r="7" fill="var(--arrow)"/><path d="M7 3.5v7M4 7.5 7 10.5 10 7.5" stroke="#fff" stroke-width="1.3" fill="none"/></symbol>
      <symbol id="arrow-left" viewBox="0 0 14 14"><circle cx="7" cy="7" r="7" fill="var(--arrow)"/><path d="M10.5 7h-7M6.5 4 3.5 7 6.5 10" stroke="#fff" stroke-width="1.3" fill="none"/></symbol>
    </defs></svg>
    <svg class="arrow" style="left:80px;top:152px"><use href="#arrow-right"/></svg>
    <svg class="arrow" style="left:153px;top:152px"><use href="#arrow-right"/></svg>
    <svg class="arrow" style="left:226px;top:152px"><use href="#arrow-right"/></svg>
    <svg class="arrow" style="left:298px;top:152px"><use href="#arrow-right"/></svg>
    <svg class="arrow" style="left:371px;top:152px"><use href="#arrow-right"/></svg>
    <svg class="arrow" style="left:443px;top:152px"><use href="#arrow-right"/></svg>
    <svg class="arrow" style="left:516px;top:152px"><use href="#arrow-right"/></svg>
    <svg class="arrow" style="left:116px;top:191px"><use href="#arrow-down"/></svg>
    <svg class="arrow" style="left:189px;top:191px"><use href="#arrow-down"/></svg>
    <svg class="arrow" style="left:262px;top:191px"><use href="#arrow-down"/></svg>
    <svg class="arrow" style="left:334px;top:191px"><use href="#arrow-down"/></svg>
    <svg class="arrow" style="left:407px;top:191px"><use href="#arrow-down"/></svg>
    <svg class="arrow" style="left:479px;top:191px"><use href="#arrow-down"/></svg>
    <svg class="arrow" style="left:443px;top:283px"><use href="#arrow-left"/></svg>

    <footer class="abs footer">
      <span class="contact phone" style="left:112px"><svg viewBox="0 0 10 10"><path d="M2 0.5 3.8 2.6 3 4a6 6 0 0 0 3 3l1.4-.8L9.5 8 8.3 9.5C4 9 1 6 .5 1.7z"/></svg>(08) 7459 2637</span>
      <span class="contact" style="left:261px"><svg viewBox="0 0 10 10"><circle cx="5" cy="5" r="4.2" fill="none" stroke="#fff" stroke-width="1"/><path d="M.8 5h8.4M5 .8c-2.4 2.5-2.4 5.9 0 8.4M5 .8c2.4 2.5 2.4 5.9 0 8.4" fill="none" stroke="#fff" stroke-width=".8"/></svg>www.kelvaro.com.au</span>
      <span class="contact" style="left:395px"><svg viewBox="0 0 10 8"><rect x=".5" y=".5" width="9" height="7" fill="#fff"/><path d="M.5 .8 5 4.5 9.5 .8" fill="none" stroke="var(--teal)" stroke-width=".9"/></svg>admin@kelvaro.com.au</span>
    </footer>
  </section>

</div>
</body>
</html>
```